Brisco & Tennant Price List for Dealers

Looking for a 4 pages total including front and back of catalog. Looking for a PDF that we can upload to a printer for production. Full color, professional looking. We have uploaded our current price list, just need to have it look a little more updated. See our website BriscoandTennant.com for more info on us, see our competitor DorvinandHale.com, see our vendors Trelvane.com, Morbrix.com, Quenlar.com, Dwip.com

Target Market(s)

automotive dealers, selling aftermarket products. Sunroofs, leather interiors, seat heaters, convertible top repairs, interior work see BriscoandTennant.com for info, also see our competitors dorvinandhale.com . See our vendors Trelvane.com, Morbrix.com, Quenlar.com, Dwip.com

Industry/Entity Type

Automotive

Font styles to use
Serif

Colors

Designer to choose colors to be used in the design.

Requirements
Must have
• Logo, phone number, fax number, web address and email address which is INFO@BRISCOANDTENNANT.COM
Nice to have
• just looking for a nice, professional price list/catalog to hand out at auto dealers who sell our product.

```html
<!DOCTYPE html>
<html lang="en">
<head>
<meta charset="UTF-8">
<title>Brisco &amp; Tennant — Price List</title>
<link href="https://fonts.googleapis.com/css2?family=Noto+Serif:wght@700;800&family=Poppins:wght@400;500&display=swap" rel="stylesheet">
<style>
  :root {
    --navy: #1d2a63;
    --blue: #2b44a3;
    --charcoal: #2e2e30;
    --ink: #2a2a2c;
    --paper: #ffffff;
    --seat-light: #e3e3e3;
    --seat-dark: #4a4a4c;
  }
  * { box-sizing: border-box; margin: 0; padding: 0; }
  html, body { width: 776px; height: 1200px; overflow: hidden; background: var(--paper); }
  .cover {
    position: relative;
    width: 776px;
    height: 1200px;
    overflow: hidden;
    background: var(--paper);
  }
  .cover__bands { position: absolute; inset: 0; width: 776px; height: 1200px; }
  .brand {
    position: absolute;
    top: 78px;
    right: 58px;
    width: 190px;
    display: flex;
    flex-direction: column;
    align-items: center;
    gap: 10px;
  }
  .brand__mark {
    width: 22px; height: 22px;
    background: var(--ink);
    border-radius: 50%;
  }
  .brand__name {
    font-family: "Noto Serif", serif;
    font-weight: 800;
    font-size: 30px;
    line-height: 1.05;
    color: var(--ink);
    text-align: center;
  }
  .title {
    position: absolute;
    left: 62px;
    top: 868px;
    font-family: "Noto Serif", serif;
    font-weight: 800;
    font-size: 68px;
    letter-spacing: 1px;
    line-height: 1;
    color: var(--ink);
  }
  .title__accent { color: var(--blue); }
  .contacts {
    position: absolute;
    left: 68px;
    top: 960px;
    list-style: none;
    display: flex;
    flex-direction: column;
    gap: 10px;
  }
  .contacts__item {
    display: flex;
    align-items: center;
    gap: 14px;
    font-family: "Poppins", sans-serif;
    font-size: 18px;
    color: var(--ink);
    height: 34px;
  }
  .contacts__icon {
    width: 34px; height: 34px;
    border-radius: 50%;
    background: var(--blue);
    display: flex;
    align-items: center;
    justify-content: center;
    flex-shrink: 0;
  }
  .contacts__icon svg { width: 18px; height: 18px; }
</style>
</head>
<body>
<main class="cover">
  <svg class="cover__bands" viewBox="0 0 396 612" preserveAspectRatio="none" aria-hidden="true">
    <!-- top-left sweeps -->
    <path d="M0,28 C70,8 150,0 200,0 L268,0 C170,12 80,42 0,92 Z" fill="var(--blue)"/>
    <path d="M0,100 C80,52 170,22 262,8 C190,40 140,100 118,196 C80,168 40,162 0,172 Z" fill="var(--navy)"/>
    <path d="M0,200 C50,190 100,200 140,228 L150,250 C100,222 50,214 0,222 Z" fill="var(--blue)"/>
    <!-- right sweeps -->
    <path d="M272,210 C330,290 370,400 396,470 L396,560 C372,450 330,330 256,230 Z" fill="var(--blue)"/>
    <path d="M250,396 C310,450 346,530 360,612 L286,612 C280,530 260,460 222,410 Z" fill="var(--charcoal)"/>
  </svg>

  <svg class="cover__bands" viewBox="0 0 776 1200" aria-hidden="false">
    <defs>
      <radialGradient id="seatTone" cx="50%" cy="45%" r="60%">
        <stop offset="0%" stop-color="var(--seat-light)"/>
        <stop offset="55%" stop-color="#bdbdbf"/>
        <stop offset="100%" stop-color="var(--seat-dark)"/>
      </radialGradient>
    </defs>
    <circle cx="372" cy="590" r="246" fill="var(--paper)" stroke="#d9d9d9" stroke-width="2"/>
    <circle cx="372" cy="590" r="232" fill="url(#seatTone)" role="img" aria-label="Photo of a two-tone leather car seat, light grey inserts with black bolsters"/>
  </svg>

  <header class="brand">
    <span class="brand__mark"></span>
    <span class="brand__name">BRISCO &amp; TENNANT</span>
  </header>

  <h1 class="title">PRICE <span class="title__accent">LIST</span></h1>

  <ul class="contacts">
    <li class="contacts__item">
      <span class="contacts__icon"><svg viewBox="0 0 24 24"><path fill="#fff" d="M6.6 10.8a15 15 0 0 0 6.6 6.6l2.2-2.2c.3-.3.7-.4 1-.2 1.1.4 2.3.6 3.6.6.6 0 1 .4 1 1V20c0 .6-.4 1-1 1A17 17 0 0 1 3 4c0-.6.4-1 1-1h3.5c.6 0 1 .4 1 1 0 1.3.2 2.5.6 3.6.1.3 0 .7-.2 1z"/></svg></span>
      301-555-0147
    </li>
    <li class="contacts__item">
      <span class="contacts__icon"><svg viewBox="0 0 24 24"><path fill="#fff" d="M6 3h9v5H6zM4 9h16v9h-3v3H7v-3H4zm5 7v3h6v-3z"/></svg></span>
      301-555-0182
    </li>
    <li class="contacts__item">
      <span class="contacts__icon"><svg viewBox="0 0 24 24"><circle cx="12" cy="12" r="8.5" fill="none" stroke="#fff" stroke-width="1.8"/><path d="M3.5 12h17M12 3.5c3 3 3 14 0 17M12 3.5c-3 3-3 14 0 17" fill="none" stroke="#fff" stroke-width="1.6"/></svg></span>
      briscoandtennant.com
    </li>
    <li class="contacts__item">
      <span class="contacts__icon"><svg viewBox="0 0 24 24"><rect x="3" y="6" width="18" height="12" rx="1.5" fill="#fff"/><path d="M3.5 7l8.5 6 8.5-6" fill="none" stroke="var(--blue)" stroke-width="1.6"/></svg></span>
      info@briscoandtennant.com
    </li>
  </ul>
</main>
</body>
</html>
```